Email Notification & Marketing Templates

I want to start with something like a newsletter or informational email, but i need Top Tips to Detect Phishing Scams. Something that i can send to users so they can follow it when receiving or exchanging emails. I will also need promotional items for my company that i can send to customers as well. It can be based on on our website PLVORIX.COM

Will also need:
newsletters
announcements
marketing emails
alerts
security notifications

Examples:Items such as Security Awareness Poster Series
Phishing Awareness
Password Security
Email Attachments
QR Code scams
Public WiFi safety

```html
<!DOCTYPE html>
<html lang="en">
<head>
<meta charset="utf-8">
<title>Plvorix – More Than IT Support</title>
<link rel="stylesheet" href="https://fonts.googleapis.com/css2?family=Outfit:wght@400;500;600;700&display=swap">
<style>
  :root {
    --page-bg: #383838;
    --paper: #ffffff;
    --paper-shade: #f1f1f1;
    --ink: #1e1e1e;
    --green-bright: #8fd63a;
    --green-mid: #5fb32a;
    --green-deep: #1d7a1a;
    --green-text: #3f9e1e;
    --band-dark: #0b2806;
    --frame-grey: #d4d4d4;
    --white: #ffffff;
  }
  * { margin: 0; padding: 0; box-sizing: border-box; }
  html, body {
    width: 1011px; height: 1200px; overflow: hidden;
    background: var(--page-bg);
    font-family: "Outfit", sans-serif;
  }
  .flyer {
    position: absolute; left: 115px; top: 15px;
    width: 780px; height: 1170px;
    background: var(--paper); overflow: hidden;
  }
  .flyer-art { position: absolute; inset: 0; width: 780px; height: 1170px; }

  .brand {
    position: absolute; left: 30px; top: 58px;
    display: flex; align-items: center; gap: 12px;
  }
  .brand-name {
    font-weight: 700; font-size: 52px; letter-spacing: 1px;
    color: var(--green-text); line-height: 1;
  }
  .brand-mark { width: 26px; height: 26px; background: var(--green-text); }

  .headline {
    position: absolute; left: 32px; top: 206px;
    font-weight: 700; font-size: 53px; line-height: 67px;
    color: var(--ink);
  }
  .headline .accent { color: var(--green-text); }

  .section-title {
    position: absolute; left: 15px; top: 544px;
    font-weight: 700; font-size: 42px; line-height: 52px;
    color: var(--green-mid);
  }

  .service { position: absolute; width: 290px; color: var(--white); }
  .service-icon {
    width: 55px; height: 51px; border-radius: 5px;
    background: var(--white);
    display: flex; align-items: center; justify-content: center;
  }
  .service-name {
    margin-top: 12px;
    font-weight: 700; font-size: 20px; line-height: 26px;
  }
  .service-text {
    margin-top: 8px;
    font-weight: 400; font-size: 14px; line-height: 24.4px;
  }
  .service--security { left: 30px; top: 633px; }
  .service--managed { left: 30px; top: 871px; }
  .service--consulting { left: 335px; top: 871px; width: 320px; }

  .contact-bar {
    position: absolute; left: 26px; top: 1110px;
    width: 727px; height: 38px;
    background: var(--white);
    clip-path: polygon(0 0, 100% 0, 100% 100%, 12px 100%);
    border-radius: 0 10px 10px 0;
    display: flex; align-items: center;
    color: var(--ink); font-weight: 500;
  }
  .contact-item { position: absolute; display: flex; align-items: center; gap: 6px; font-size: 14px; }
  .contact-item--phone { left: 20px; font-weight: 600; }
  .contact-item--email { left: 149px; }
  .contact-item--web { left: 292px; }
  .contact-item--address { left: 403px; font-size: 10.5px; }
  .contact-icon { width: 18px; height: 18px; flex: none; }
</style>
</head>
<body>
<main class="flyer">
  <svg class="flyer-art" viewBox="0 0 780 1170" aria-hidden="false">
    <defs>
      <linearGradient id="greenField" x1="1" y1="0" x2="0" y2="1">
        <stop offset="0" stop-color="#8fd63a"/>
        <stop offset="0.55" stop-color="#4aa425"/>
        <stop offset="1" stop-color="#1d7a1a"/>
      </linearGradient>
      <linearGradient id="greenDiamond" x1="0" y1="0" x2="1" y2="1">
        <stop offset="0" stop-color="#a6ea45"/>
        <stop offset="1" stop-color="#2f8f1c"/>
      </linearGradient>
      <linearGradient id="photoDesk" x1="0" y1="0" x2="1" y2="1">
        <stop offset="0" stop-color="#c9a890"/><stop offset="1" stop-color="#3b4656"/>
      </linearGradient>
      <linearGradient id="photoWarehouse" x1="0" y1="0" x2="1" y2="1">
        <stop offset="0" stop-color="#8a8f97"/><stop offset="1" stop-color="#c8b49a"/>
      </linearGradient>
      <linearGradient id="photoMonitors" x1="0" y1="0" x2="1" y2="1">
        <stop offset="0" stop-color="#1d2633"/><stop offset="1" stop-color="#5a6b82"/>
      </linearGradient>
      <linearGradient id="photoMeeting" x1="0" y1="0" x2="0" y2="1">
        <stop offset="0" stop-color="#dcd6da"/><stop offset="1" stop-color="#c9772f"/>
      </linearGradient>
      <linearGradient id="illustrationFill" x1="0" y1="0" x2="0" y2="1">
        <stop offset="0" stop-color="#e6efdf"/><stop offset="1" stop-color="#f7f7f7"/>
      </linearGradient>
    </defs>

    <!-- soft background panel -->
    <polygon points="0,76 416,288 187,496 0,385" fill="var(--paper-shade)"/>

    <!-- green lower field -->
    <polygon points="0,473 780,1075 780,1170 0,1170" fill="url(#greenField)"/>

    <!-- section band -->
    <polygon points="0,535 292,535 353,606 0,606" fill="var(--band-dark)"/>

    <!-- corner accents -->
    <polygon points="725,0 780,0 780,89 728,29" fill="var(--green-bright)"/>
    <polygon points="780,250 780,318 762,286" fill="var(--green-bright)"/>

    <!-- large green diamond -->
    <rect x="-154" y="-154" width="308" height="308" rx="40" fill="url(#greenDiamond)" transform="translate(594 610) rotate(45)"/>
    <polygon points="405,671 520,490 660,490 780,672 597,762" fill="url(#illustrationFill)" role="img" aria-label="Isometric illustration of servers, a laptop and network nodes on a platform"/>

    <!-- photo diamond: support agent -->
    <rect x="-104" y="-104" width="209" height="209" rx="26" fill="var(--frame-grey)" transform="translate(432 96) rotate(45)"/>
    <rect x="-95" y="-95" width="191" height="191" rx="22" fill="url(#photoDesk)" transform="translate(432 96) rotate(45)" role="img" aria-label="Photo of a support technician on the phone at a desk with monitors"/>

    <!-- photo diamond: warehouse camera -->
    <rect x="-68" y="-68" width="137" height="137" rx="18" fill="var(--frame-grey)" transform="translate(711 157) rotate(45)"/>
    <rect x="-61" y="-61" width="123" height="123" rx="15" fill="url(#photoWarehouse)" transform="translate(711 157) rotate(45)" role="img" aria-label="Photo of a security camera in a warehouse"/>

    <!-- photo diamond: monitoring screens -->
    <rect x="-78" y="-78" width="157" height="157" rx="22" fill="var(--green-bright)" transform="translate(600 264) rotate(45)"/>
    <rect x="-70" y="-70" width="141" height="141" rx="18" fill="url(#photoMonitors)" transform="translate(600 264) rotate(45)" role="img" aria-label="Photo of network monitoring screens on a desk"/>

    <!-- photo diamond: meeting room -->
    <rect x="-83" y="-83" width="167" height="167" rx="22" fill="var(--frame-grey)" transform="translate(708 426) rotate(45)"/>
    <rect x="-75" y="-75" width="151" height="151" rx="18" fill="url(#photoMeeting)" transform="translate(708 426) rotate(45)" role="img" aria-label="Photo of a meeting room with a dashboard on a wall screen"/>
  </svg>

  <div class="brand">
    <span class="brand-name">PLVORIX</span>
    <span class="brand-mark"></span>
  </div>

  <h1 class="headline">
    <span class="accent">More Than IT<br>Support.</span><br>
    We're Your IT<br>Partner.
  </h1>

  <h2 class="section-title">WHAT WE DO</h2>

  <section class="service service--security">
    <div class="service-icon">
      <svg width="34" height="34" viewBox="0 0 34 34" fill="none" stroke="#2f8f1c" stroke-width="2">
        <rect x="10" y="15" width="14" height="11" rx="2" fill="#2f8f1c"/>
        <path d="M13 15v-4a4 4 0 0 1 8 0v4"/>
        <path d="M4 12h5M25 12h5M4 22h5M25 22h5M17 26v5"/>
        <circle cx="3" cy="12" r="1.5"/><circle cx="31" cy="12" r="1.5"/>
        <circle cx="3" cy="22" r="1.5"/><circle cx="31" cy="22" r="1.5"/>
      </svg>
    </div>
    <h3 class="service-name">CYBERSECURITY</h3>
    <p class="service-text">Protecting your business is our top priority.<br>We offer robust cybersecurity solutions<br>designed to safeguard your data and<br>infrastructure from threats, ensuring<br>peace of mind.</p>
  </section>

  <section class="service service--managed">
    <div class="service-icon">
      <svg width="36" height="36" viewBox="0 0 36 36" fill="none" stroke="#2f8f1c" stroke-width="2.5">
        <circle cx="20" cy="13" r="6"/><circle cx="20" cy="13" r="2" fill="#2f8f1c"/>
        <path d="M20 3v3M20 20v3M10 13h3M27 13h3"/>
        <path d="M4 28c6 0 8-4 14-3l8-3c2 0 2 2 0 3l-8 5H4z" fill="#2f8f1c" stroke="none"/>
      </svg>
    </div>
    <h3 class="service-name">MANAGED IT SERVICES</h3>
    <p class="service-text">Our proactive IT management keeps your<br>systems running smoothly, so you can focus<br>on what you do best. We monitor, maintain,<br>and optimize your IT infrastructure to<br>prevent issues before they arise.</p>
  </section>

  <section class="service service--consulting">
    <div class="service-icon">
      <svg width="34" height="34" viewBox="0 0 34 34" fill="none">
        <circle cx="17" cy="17" r="11" fill="#2f8f1c"/>
        <path d="M17 2v5M17 27v5M2 17h5M27 17h5M6 6l4 4M24 24l4 4M28 6l-4 4M6 28l4-4" stroke="#2f8f1c" stroke-width="4"/>
        <circle cx="17" cy="17" r="7" fill="#fff"/>
        <path d="M14 14l-3 3 3 3M20 14l3 3-3 3M18 13l-2 8" stroke="#2f8f1c" stroke-width="1.5"/>
      </svg>
    </div>
    <h3 class="service-name">IT CONSULTING</h3>
    <p class="service-text">With our expert guidance, navigate the<br>ever-evolving landscape of technology to make<br>informed decisions that propel your business<br>forward. We tailor our advice to suit your<br>strategic goals and operational needs.</p>
  </section>

  <footer class="contact-bar">
    <span class="contact-item contact-item--phone">
      <svg class="contact-icon" viewBox="0 0 18 18"><rect x="3" y="3" width="12" height="12" transform="rotate(45 9 9)" fill="#4aa425"/><path d="M7 6l1 2-1 1a5 5 0 0 0 2 2l1-1 2 1-1 1.5c-3 0-5.5-2.5-5.5-5.5z" fill="#fff"/></svg>
      (555) 014-2290
    </span>
    <span class="contact-item contact-item--email">
      <svg class="contact-icon" viewBox="0 0 18 18"><rect x="3" y="3" width="12" height="12" transform="rotate(45 9 9)" fill="#4aa425"/><rect x="6" y="7" width="6" height="4.5" fill="#fff"/><path d="M6 7l3 2.5L12 7" stroke="#4aa425" stroke-width="0.8" fill="none"/></svg>
      info@plvorix.com.
    </span>
    <span class="contact-item contact-item--web">
      <svg class="contact-icon" viewBox="0 0 18 18"><rect x="3" y="3" width="12" height="12" transform="rotate(45 9 9)" fill="#4aa425"/><circle cx="9" cy="9" r="3.2" fill="none" stroke="#fff" stroke-width="1"/><path d="M5.8 9h6.4M9 5.8v6.4" stroke="#fff" stroke-width="0.8"/></svg>
      plvorix.com
    </span>
    <span class="contact-item contact-item--address">
      <svg class="contact-icon" viewBox="0 0 18 18"><rect x="3" y="3" width="12" height="12" transform="rotate(45 9 9)" fill="#4aa425"/><circle cx="9" cy="9" r="3.2" fill="none" stroke="#fff" stroke-width="1"/><path d="M5.8 9h6.4M9 5.8v6.4" stroke="#fff" stroke-width="0.8"/></svg>
      418 Birchway Ln. Unit 3 &amp; 4 Fairmont, KY 40299
    </span>
  </footer>
</main>
</body>
</html>
```